Web Infographic for Life Insurance

We need an infographic for our insurance site based on research commissioned previously. We have a report of statistics on the cost and coverage of life insurance in 1999 vs 2019. What we're looking for is an infographic that presents these statistics in an entertaining and informative way. Site is CoverLantern.com
Target Market(s)
Americans ages 30-65 interested in life insurance.
Industry/Entity Type
Insurance
Number of Pages Required
1 page
Font styles to use
Sans Serif
Decorative
Colors
85cae6
faa54b
ffffff
86cfc6
Requirements
Must have
- Long vertical infographic readable on mobile devices
Nice to have
- Footnote references
Should not have
- Extremely small text
- Any brand logos or trademarked imagery other than for coverlantern

```html
<!DOCTYPE html>
<html lang="en">
<head>
<meta charset="utf-8">
<title>The Cost and Coverage of Life Insurance in 1999 vs 2019 | CoverLantern</title>
<link href="https://fonts.googleapis.com/css2?family=Sora:wght@600;700;800&family=Roboto:wght@300;400;500;700&display=swap" rel="stylesheet">
<style>
  :root{
    --sky:#85cae6;
    --orange:#faa54b;
    --orange-deep:#f4873a;
    --mint:#86cfc6;
    --white:#ffffff;
    --ink:#1c1c24;
    --text:#555a60;
    --brand:#1f6fbf;
    --gold:#c8862b;
    --navy:#143049;
    --mist:#edf2f2;
    --cream:#fdf4ea;
    --green:#5aa84a;
    --red:#d8372f;
  }
  *{box-sizing:border-box;margin:0;padding:0}
  html,body{width:1200px;height:4141px;overflow:hidden}
  body{position:relative;background:var(--white);font-family:"Roboto",sans-serif;color:var(--text)}
  .abs{position:absolute}
  .band{position:absolute;left:0;width:1200px}
  .heading{font-family:"Sora",sans-serif;font-weight:700;color:var(--ink);line-height:1.22}

  /* header */
  .hero{top:0;height:900px;background:linear-gradient(180deg,#a9dcf3 0%,#bfe6f6 60%,#cdeaf6 100%)}
  .building{left:850px;top:0;width:350px;height:810px;background:linear-gradient(135deg,#2a6ee0 0%,#1fa6ea 55%,#18d0f2 100%)}
  .logo{left:85px;top:34px;font-family:"Sora",sans-serif;font-weight:600;font-size:36px;color:var(--brand);letter-spacing:-.5px}
  .title{left:85px;top:112px;font-size:42px}
  .title .light{font-family:"Roboto",sans-serif;font-weight:300;display:block;font-size:41px;color:#2b2f36}
  .intro{left:87px;top:246px;width:668px;font-size:17px;line-height:34px;color:#5a6570}
  .summary{left:85px;top:436px;font-family:"Sora",sans-serif;font-weight:800;font-size:38px;color:#1a6aa8;letter-spacing:.5px}
  .years{left:85px;top:496px;font-family:"Sora",sans-serif;font-weight:700;font-size:30px;color:var(--gold)}
  .pill{top:578px;width:338px;height:124px;background:var(--white);border-radius:62px;box-shadow:0 6px 18px rgba(40,90,130,.15)}
  .pill .badge{position:absolute;left:10px;top:10px;width:104px;height:104px;border-radius:50%;border:4px solid #d6ecf6;background:radial-gradient(circle,#dff1f9 0%,#c7e5f2 100%)}
  .pill .big{position:absolute;left:142px;top:20px;font-size:23px;font-weight:500;color:var(--orange-deep)}
  .pill .small{position:absolute;left:142px;top:62px;font-size:14.5px;line-height:22px;color:#3b3f45}
  .mid-label{left:458px;top:598px;font-size:16.5px;color:#2b2f36}
  .mid-value{left:458px;top:656px;font-size:22px;font-weight:500;color:var(--gold)}
  .mid-note{left:458px;top:698px;font-size:14px;line-height:22px;color:#3b3f45}
  .mid-note b{font-weight:500;color:#1a6aa8}

  .scroll{width:26px;height:44px}

  /* purchases */
  .h-purchases{left:84px;top:996px;font-size:40px;width:800px}
  .people{left:88px;top:1204px;width:402px;height:402px;border-radius:18px;background:linear-gradient(180deg,#f2d7c2 0%,#e9a96a 40%,#4a7fb3 75%,#2c3a4a 100%);opacity:.9}
  .map{left:618px;top:1237px;width:378px;height:233px;border-radius:14px;background:linear-gradient(135deg,#3a83d6,#1f5fb6)}
  .stat-big{font-family:"Sora",sans-serif;font-weight:700;font-size:25px;color:var(--ink)}
  .stat-note{font-size:11.5px;line-height:17px}

  /* numbers */
  .h-numbers{left:86px;top:1858px;font-size:40px}
  .check-list{list-style:none;font-size:14.5px;line-height:34px;color:#4a4f55}
  .check-list li{position:relative;padding-left:30px}
  .check-list li::before{content:"";position:absolute;left:0;top:11px;width:11px;height:11px;border-radius:50%;border:2px solid var(--sky);background:#dff0f8}
  .check-list sup{color:var(--orange-deep);font-size:11px}
  .numbers-list{left:86px;top:1994px;width:522px}
  .family-art{left:660px;top:1872px;width:540px;height:360px;border-radius:20px 0 0 20px;background:linear-gradient(160deg,#dcebf5 0%,#cfe3f0 45%,#c8dceb 100%)}

  /* cost */
  .cream{top:2330px;height:760px;background:var(--cream)}
  .h-cost{left:575px;top:2388px;font-size:40px}
  .cost-list{left:577px;top:2522px;width:540px}
  .chart{left:20px;top:2420px}

  /* reasons */
  .h-reasons{left:0;top:3262px;width:1200px;text-align:center;font-size:40px}
  .reasons-sub{left:150px;top:3380px;width:900px;text-align:center;font-size:14.5px;line-height:34px;color:#555}
  .bubble{position:absolute;width:160px;height:160px;border-radius:50%;display:flex;flex-direction:column;align-items:center;justify-content:center;text-align:center;color:var(--white);padding:0 10px}
  .bubble b{font-family:"Sora",sans-serif;font-weight:700;font-size:29px;line-height:36px}
  .bubble span{font-size:14.5px;line-height:26px;opacity:.95}
  .b-blue{background:linear-gradient(135deg,var(--sky) 0%,#6fb6dd 100%)}
  .b-mint{background:linear-gradient(135deg,#9ad9cf 0%,#6fc0b4 100%)}
  .b-orange{background:linear-gradient(135deg,var(--orange) 0%,var(--orange-deep) 100%)}

  /* footer */
  .footer-art{left:708px;top:3990px;width:142px;height:70px;border-radius:12px;background:linear-gradient(180deg,#d83a44,#b51d2a)}
  .copyright{left:0;top:4092px;width:1200px;text-align:center;font-size:11.5px;color:#e6eef5}
</style>
</head>
<body>

<!-- ===== Header ===== -->
<section class="band hero"></section>
<div class="abs building" role="img" aria-label="Illustration of a tall blue glass office tower"></div>
<svg class="abs" style="left:0;top:760px" width="1200" height="160" viewBox="0 0 1200 160" aria-hidden="true">
  <path d="M0 40 C80 20 120 70 200 70 C300 70 330 30 430 45 C520 60 540 100 600 100 C660 100 700 40 820 45 C930 50 960 90 1040 70 C1110 52 1150 40 1200 55 L1200 160 L0 160Z" fill="#ffffff"/>
</svg>

<div class="abs logo">CoverLantern</div>
<h1 class="abs heading title">The Cost and Coverage of Life<span class="light">Insurance in 1999 vs 2019</span></h1>
<p class="abs intro">CoverLantern was created to make insurance easy to find, easy to buy, and easy to understand. Our staff has done an in-depth review of the best options for home, health, medicare, and more. Browse hundreds of guides, or build a free Lantern Report to find your next policy.</p>
<h2 class="abs summary">SUMMARY STATISTICS</h2>
<div class="abs years">1992-1997</div>

<div class="abs pill" style="left:88px">
  <div class="badge" role="img" aria-label="Illustration of a group of people with rising arrows"></div>
  <div class="big">3.62 (4.91)</div>
  <div class="small">Type Term Premium<br>/($1000 of Face)</div>
</div>
<div class="abs mid-label">Length of policy</div>
<svg class="abs" style="left:421px;top:632px" width="212" height="16" viewBox="0 0 212 16" aria-hidden="true">
  <line x1="0" y1="8" x2="204" y2="8" stroke="#c9d3da" stroke-width="2"/>
  <path d="M198 2 L208 8 L198 14" fill="none" stroke="#c9d3da" stroke-width="2"/>
</svg>
<div class="abs mid-value">2.27</div>
<div class="abs mid-note">Non-Smoker &nbsp;: <b>774 (.418)</b><br>Male 666 : <b>(.472)</b></div>
<div class="abs pill" style="left:631px">
  <div class="badge" role="img" aria-label="Illustration of banknotes and gold coins"></div>
  <div class="big">132.97 (136.41)</div>
  <div class="small">Real Amount of Policy<br>(in '000s of 1990 dollars)</div>
</div>

<svg class="abs scroll" style="left:587px;top:837px" viewBox="0 0 26 44" aria-hidden="true">
  <rect x="2" y="2" width="22" height="40" rx="11" fill="none" stroke="#222" stroke-width="2"/>
  <line x1="13" y1="9" x2="13" y2="16" stroke="#222" stroke-width="2"/>
  <path d="M8 27 L13 32 L18 27" fill="none" stroke="#222" stroke-width="2"/>
</svg>

<!-- ===== Purchases ===== -->
<h2 class="abs heading h-purchases">Number of life insurance Policy Purchases in the United States from 1998 to 2018 (in millions)</h2>
<div class="abs people" role="img" aria-label="Illustration of a diverse crowd of adults standing together"></div>
<div class="abs map" role="img" aria-label="Blue map of the United States"></div>
<div class="abs stat-big" style="left:985px;top:1344px">27.8</div>
<svg class="abs" style="left:1050px;top:1340px" width="16" height="36" viewBox="0 0 16 36" aria-hidden="true">
  <line x1="8" y1="4" x2="8" y2="36" stroke="#5aa84a" stroke-width="2"/><path d="M2 10 L8 3 L14 10" fill="none" stroke="#5aa84a" stroke-width="2"/>
</svg>
<p class="abs stat-note" style="left:985px;top:1394px;width:140px;color:var(--green)">Million life insurance policies were purchased in the United States</p>
<div class="abs stat-big" style="left:770px;top:1488px">8-15</div>
<svg class="abs" style="left:836px;top:1482px" width="16" height="38" viewBox="0 0 16 38" aria-hidden="true">
  <line x1="8" y1="0" x2="8" y2="32" stroke="#d8372f" stroke-width="2"/><path d="M2 26 L8 34 L14 26" fill="none" stroke="#d8372f" stroke-width="2"/>
</svg>
<p class="abs stat-note" style="left:708px;top:1537px;width:210px;text-align:center;color:var(--red)">The growth of the Internet has reduced term life prices by 8–15 percent</p>

<!-- ===== By the numbers ===== -->
<svg class="abs" style="left:0;top:1660px" width="1200" height="140" viewBox="0 0 1200 140" aria-hidden="true">
  <rect x="0" y="0" width="1200" height="140" fill="#ffffff"/>
  <path d="M0 130 C60 110 90 40 180 40 C280 40 330 80 430 70 C520 60 540 20 600 20 C680 20 700 70 800 70 C900 70 940 20 1040 30 C1120 38 1160 60 1200 60 L1200 140 L0 140Z" fill="#edf2f2"/>
</svg>
<section class="band" style="top:1790px;height:540px;background:var(--mist)"></section>
<svg class="abs scroll" style="left:587px;top:1708px" viewBox="0 0 26 44" aria-hidden="true">
  <rect x="2" y="2" width="22" height="40" rx="11" fill="none" stroke="#222" stroke-width="2"/>
  <line x1="13" y1="9" x2="13" y2="16" stroke="#222" stroke-width="2"/>
  <path d="M8 27 L13 32 L18 27" fill="none" stroke="#222" stroke-width="2"/>
</svg>

<h2 class="abs heading h-numbers">Life insurance by<br>The numbers</h2>
<ul class="abs check-list numbers-list">
  <li>57% &nbsp;Percent of American adults who have life insurance<sup>†</sup></li>
  <li>32% Of American adults with life insurance, the percent who only have group coverage — which usually isn't enough (and is rarely portable)<sup>†</sup></li>
  <li>10x to 12x &nbsp;The multiples of your annual income that most financial advisors recommend you need when buying life insurance for income replacement<sup>†</sup></li>
  <li>50% Percent of life insurance policies are purchased via independent agents</li>
  <li>40% Percent of life insurance policies purchased via affiliated agents (meaning they only sell products for one insurance company)<sup>†</sup></li>
</ul>
<div class="abs family-art" role="img" aria-label="Illustration of a family beside a large umbrella sheltering home, health, dental and savings icons"></div>

<!-- ===== Cost ===== -->
<section class="band cream"></section>
<h2 class="abs heading h-cost">Stats about the Cost<br>Of life Insurance</h2>
<ul class="abs check-list cost-list">
  <li>6x-10x How much more permanent life insurance (like whole life insurance) costs vs.term life insurance<sup>†</sup></li>
  <li>8% * Average percent increase in your insurance costs as you age, assuming your health stays the same<sup>†</sup></li>
  <li>30% The average cost difference between sequential health ratings (preferred vs standard, for example)<sup>†</sup></li>
  <li>2x to 3x How much rates for smokers cost vs. rates for nonsmokers(but a year after you quit smoking, most companies will offer you nonsmoker rates)<sup>†</sup></li>
  <li>50% The average difference between the least expensive and most expensive rate for the same person across insurance companies<sup>†</sup></li>
  <li>30% Percent difference between premiums for men and women(with women paying nearly 1/3 &nbsp;less than men, on average)<sup>†</sup></li>
</ul>

<svg class="abs chart" width="520" height="520" viewBox="0 0 520 520" role="img" aria-label="Bar chart comparing six cost statistics">
  <g fill="#e8e2dc">
    <rect x="56" y="14" width="44" height="430" rx="22"/>
    <rect x="129" y="14" width="44" height="430" rx="22"/>
    <rect x="204" y="14" width="44" height="430" rx="22"/>
    <rect x="281" y="14" width="44" height="430" rx="22"/>
    <rect x="356" y="14" width="44" height="430" rx="22"/>
    <rect x="432" y="14" width="44" height="430" rx="22"/>
  </g>
  <rect x="56" y="224" width="44" height="220" rx="22" fill="#9b80b2"/>
  <rect x="129" y="310" width="44" height="134" rx="22" fill="#d65a38"/>
  <rect x="204" y="172" width="44" height="272" rx="22" fill="#2f879c"/>
  <rect x="281" y="260" width="44" height="184" rx="22" fill="#4b9878"/>
  <rect x="356" y="104" width="44" height="340" rx="22" fill="#dba21c"/>
  <rect x="432" y="96" width="44" height="348" rx="22" fill="#b7c63a"/>
  <polyline points="78,174 151,232 226,136 303,218 378,76 454,66" fill="none" stroke="#777" stroke-width="2"/>
  <g fill="#2f879c" stroke="#fff" stroke-width="2">
    <circle cx="78" cy="174" r="6"/><circle cx="151" cy="232" r="6"/><circle cx="226" cy="136" r="6"/>
    <circle cx="303" cy="218" r="6"/><circle cx="378" cy="76" r="6"/><circle cx="454" cy="66" r="6"/>
  </g>
  <g font-family="Roboto,sans-serif" font-style="italic" font-size="13" fill="#444">
    <text x="70" y="164">01</text><text x="143" y="252">02</text><text x="218" y="126">03</text>
    <text x="295" y="208">04</text><text x="370" y="64">05</text><text x="446" y="56">06</text>
  </g>
  <g font-family="Roboto,sans-serif" font-size="7" fill="#c98a2b">
    <text x="56" y="462">Whole vs term</text><text x="56" y="471">cost multiple</text>
    <text x="129" y="462">Yearly rise</text><text x="129" y="471">with age</text>
    <text x="204" y="462">Health rating</text><text x="204" y="471">cost gap</text>
    <text x="281" y="462">Smoker rate</text><text x="281" y="471">multiple</text>
    <text x="356" y="462">Spread across</text><text x="356" y="471">insurers</text>
    <text x="432" y="462">Gender premium</text><text x="432" y="471">difference</text>
  </g>
  <g>
    <circle cx="225" cy="495" r="4" fill="#9b80b2"/><circle cx="236" cy="495" r="4" fill="#d65a38"/>
    <circle cx="247" cy="495" r="4" fill="#2f879c"/><circle cx="258" cy="495" r="4" fill="#4b9878"/>
    <circle cx="269" cy="495" r="4" fill="#dba21c"/><circle cx="280" cy="495" r="4" fill="#b7c63a"/>
  </g>
</svg>

<!-- ===== Reasons ===== -->
<svg class="abs" style="left:0;top:3000px" width="1200" height="160" viewBox="0 0 1200 160" aria-hidden="true">
  <path d="M0 40 C80 10 140 70 240 60 C340 50 380 20 470 40 C540 56 560 100 600 100 C650 100 680 40 780 45 C880 50 920 90 1010 70 C1090 50 1150 30 1200 40 L1200 160 L0 160Z" fill="#ffffff"/>
</svg>
<svg class="abs scroll" style="left:587px;top:3067px" viewBox="0 0 26 44" aria-hidden="true">
  <rect x="2" y="2" width="22" height="40" rx="11" fill="none" stroke="#222" stroke-width="2"/>
  <line x1="13" y1="9" x2="13" y2="16" stroke="#222" stroke-width="2"/>
  <path d="M8 27 L13 32 L18 27" fill="none" stroke="#222" stroke-width="2"/>
</svg>

<h2 class="abs heading h-reasons">Top reasons for buying life<br>Insurance in the U.S.</h2>
<p class="abs reasons-sub">According to a 2019 report from trade research organization Northfield Market Research and the non-profit organization Cover Matters, these are the most common reasons Americans said they bought life insurance:</p>

<div class="bubble b-blue" style="left:89px;top:3503px"><b>37%</b><span>Income replacement</span></div>
<div class="bubble b-mint" style="left:260px;top:3503px"><b>30%</b><span>Burial/final expenses</span></div>
<div class="bubble b-orange" style="left:434px;top:3503px"><b>28%</b><span>Wealth transfer</span></div>
<div class="bubble b-blue" style="left:606px;top:3503px"><b>27%</b><span>Pay off mortgage</span></div>
<div class="bubble b-orange" style="left:778px;top:3503px"><b>19%</b><span>Replaced a policy</span></div>
<div class="bubble b-mint" style="left:950px;top:3488px"><b>17%</b><span>Tax advantaged save/invest</span></div>

<div class="bubble b-orange" style="left:174px;top:3686px"><b>14%</b><span>Estate taxes/liquidity</span></div>
<div class="bubble b-blue" style="left:346px;top:3686px"><b>14%</b><span>Funds for college education</span></div>
<div class="bubble b-mint" style="left:517px;top:3686px"><b>13%</b><span>Charitable gift</span></div>
<div class="bubble b-orange" style="left:691px;top:3686px"><b>8%</b><span>Supplement group coverage</span></div>
<div class="bubble b-blue" style="left:863px;top:3686px"><b>8%</b><span>Business purposes</span></div>

<!-- ===== Footer ===== -->
<svg class="abs" style="left:0;top:3940px" width="1200" height="201" viewBox="0 0 1200 201" aria-hidden="true">
  <path d="M0 10 C60 10 90 90 170 90 C260 90 290 40 380 40 C460 40 480 90 560 90 C610 90 620 40 650 40 C720 40 740 95 830 95 C920 95 960 40 1050 40 C1120 40 1160 80 1200 80 L1200 201 L0 201Z" fill="#143049"/>
</svg>
<svg class="abs scroll" style="left:587px;top:3990px" viewBox="0 0 26 44" aria-hidden="true">
  <rect x="2" y="2" width="22" height="40" rx="11" fill="none" stroke="#ffffff" stroke-width="2"/>
  <line x1="13" y1="9" x2="13" y2="16" stroke="#ffffff" stroke-width="2"/>
  <path d="M8 27 L13 32 L18 27" fill="none" stroke="#ffffff" stroke-width="2"/>
</svg>
<div class="abs footer-art" role="img" aria-label="Illustration of a red umbrella"></div>
<p class="abs copyright">All Rights Reserved by CoverLantern © 2020</p>

</body>
</html>
```